Enterteinment new company in Costa Rica who wants to attract international artists

We need a business design for s new company from Costa Rica Called The Copper Lanterns. Our core business is Produce Alternative Rock Concerts. We would like to see a very creative business card connected to music ideas. Our logo is Black so we would like to see not too many colors on it. Silver letters would be great combined with black.

Target Market(s)

Entertainment

Industry/Entity Type

Entertainment

Contact Information for Business Card

We would like something different, creative.

Font styles to use
Other font styles liked:
• voltaire

Colors
000000
ffffff

Requirements
Must have
• We are looking for a creative business card
Nice to have
• liked to music

```html
<!DOCTYPE html>
<html lang="en">
<head>
<meta charset="utf-8">
<title>The Copper Lanterns — Business Card</title>
<link rel="stylesheet" href="https://fonts.googleapis.com/css2?family=Lato:wght@300;400;700&display=swap">
<style>
  :root {
    --backdrop: #c9c9c9;
    --card-light: #f7f7f7;
    --card-dark: #1d1d1d;
    --ink: #2b2b2b;
    --ink-soft: #5a5a5a;
    --silver: #a9a9a9;
    --silver-soft: #8a8a8a;
  }
  * { margin: 0; padding: 0; box-sizing: border-box; }
  html, body { width: 1200px; height: 900px; overflow: hidden; }
  body {
    background: var(--backdrop);
    font-family: "Lato", Arial, sans-serif;
    position: relative;
  }
  .card {
    position: absolute;
    top: 307px;
    width: 500px;
    height: 286px;
    box-shadow: 0 6px 18px rgba(0,0,0,0.18);
  }
  .card--front { left: 70px; background: var(--card-light); color: var(--ink); }
  .card--back { left: 630px; background: var(--card-dark); }

  .contact { position: absolute; left: 40px; top: 38px; }
  .contact__name { font-size: 22px; font-weight: 700; letter-spacing: 0.2px; }
  .contact__role { font-size: 12px; color: var(--ink-soft); margin-top: 2px; }
  .contact__list { margin-top: 26px; font-size: 12.5px; line-height: 1.35; }
  .contact__label { color: var(--ink-soft); }
  .contact__value { margin-bottom: 2px; }

  .brand { position: absolute; display: flex; flex-direction: column; align-items: center; }
  .brand__mark { width: 46px; height: 46px; border-radius: 50%; }
  .brand__name {
    font-weight: 300;
    font-size: 11px;
    letter-spacing: 5px;
    text-transform: uppercase;
    margin-top: 14px;
    white-space: nowrap;
  }
  .card--front .brand { right: 34px; top: 150px; }
  .card--front .brand__mark { background: var(--ink); }
  .card--front .brand__name { color: var(--silver-soft); }

  .card--back .brand { left: 0; right: 0; top: 96px; }
  .card--back .brand__mark { width: 56px; height: 56px; background: var(--silver); }
  .card--back .brand__name { color: var(--silver); font-size: 13px; letter-spacing: 7px; margin-top: 18px; }
</style>
</head>
<body>
  <section class="card card--front">
    <div class="contact">
      <h1 class="contact__name">Mateo Alvarado</h1>
      <p class="contact__role">Managing Director</p>
      <dl class="contact__list">
        <dt class="contact__label">telephone</dt>
        <dd class="contact__value">044-210 987 654</dd>
        <dt class="contact__label">email</dt>
        <dd class="contact__value">hello@copperlanterns.cr</dd>
        <dt class="contact__label">address</dt>
        <dd class="contact__value">118 Calle Luna, San José, Costa Rica</dd>
      </dl>
    </div>
    <div class="brand">
      <span class="brand__mark"></span>
      <span class="brand__name">The Copper Lanterns</span>
    </div>
  </section>

  <section class="card card--back">
    <div class="brand">
      <span class="brand__mark"></span>
      <span class="brand__name">The Copper Lanterns</span>
    </div>
  </section>
</body>
</html>
```